Small environmental consultancy requires basic yet awesome website design by aspiring and cool desig

We are a small environmental consultancy based in Australia, we have set-out a design brief for our website, using a logo we had completed here on Mosaic Yard as well. We hope you can help us with a website!

Website must be pagelark friendly - we have reserved hosting with them already!

Number of Pages Required

4 page

Requirements
Must have
• use supplied logo
• pagelark
• follow provided brief

```html
<!DOCTYPE html>
<html lang="en">
<head>
<meta charset="utf-8">
<title>Verdant Field</title>
<link href="https://fonts.googleapis.com/css2?family=Open+Sans:wght@400;600;700;800&display=swap" rel="stylesheet">
<style>
:root{
  --green:#8dc63f;
  --green-dark:#5f9a22;
  --ink:#333;
  --muted:#666;
  --dark:#2f2f2f;
  --darker:#1f1f1f;
  --band:#4a4a4a;
  --light:#f3f3f3;
  --white:#fff;
  --client:#3a5a8c;
}
*{box-sizing:border-box;margin:0;padding:0}
html,body{width:1200px;height:2184px;overflow:hidden}
body{font-family:"Open Sans",Arial,sans-serif;color:var(--ink);background:var(--white);position:relative}

/* header */
.site-header{position:absolute;left:0;top:0;width:1200px;height:152px;background:var(--white)}
.brand{position:absolute;left:130px;top:28px;display:flex;align-items:center;gap:12px}
.brand-mark{width:52px;height:52px;border-radius:50%;border:4px solid var(--green)}
.brand-name{font-weight:800;font-size:26px;line-height:1;color:var(--green)}
.social{position:absolute;right:130px;top:6px;display:flex;gap:6px}
.social span{width:22px;height:22px;background:var(--dark);border-radius:3px}
.main-nav{position:absolute;right:130px;top:78px;display:flex}
.main-nav a{display:flex;align-items:flex-end;justify-content:center;width:78px;height:74px;padding-bottom:10px;font-size:14px;color:var(--ink);text-decoration:none;border-left:1px solid #ddd;position:relative}
.main-nav a::before{content:"";position:absolute;top:12px;left:30px;width:18px;height:18px;border-radius:3px;background:#9a9a9a}
.main-nav a.active{background:#555;color:var(--white)}
.main-nav a.active::before{background:var(--white)}

/* hero */
.hero{position:absolute;left:0;top:152px;width:1200px;height:468px;background:linear-gradient(180deg,#cfd8de 0%,#9bb0bf 35%,#56707f 70%,#3d5563 100%)}
.hero-text{position:absolute;left:520px;top:252px;width:420px;text-align:center;color:var(--white);font-weight:700;font-size:24px;line-height:1.35;text-shadow:0 1px 3px rgba(0,0,0,.5)}
.hero-arrow{position:absolute;top:218px;width:34px;height:34px;border-radius:50%;background:rgba(0,0,0,.4)}
.hero-arrow svg{display:block}

/* services */
.services{position:absolute;left:0;top:620px;width:1200px;height:540px;background:linear-gradient(180deg,#1b2a4a 0%,#35577a 30%,#6f9a3d 60%,#4f7d22 100%)}
.card{position:absolute;top:30px;width:220px;height:470px;background:var(--white);border-radius:4px;overflow:hidden;box-shadow:0 2px 8px rgba(0,0,0,.35)}
.card h3{background:var(--green);color:var(--white);font-size:12px;font-weight:700;text-align:center;height:62px;display:flex;align-items:center;justify-content:center;padding:0 10px;line-height:1.3;text-transform:uppercase}
.card-photo{margin:12px;height:170px}
.card ul{list-style:none;padding:4px 16px;font-size:12px;line-height:1.9;color:var(--muted)}
.card li::before{content:"\2022";color:var(--green);margin-right:6px}

/* welcome */
.welcome{position:absolute;left:130px;top:1190px;width:560px;height:280px}
.section-head{font-size:24px;font-weight:600;color:var(--ink)}
.section-head b{color:var(--green);font-weight:600}
.welcome p{margin-top:18px;font-size:13px;line-height:1.75;color:var(--muted)}
.btn{display:inline-block;background:var(--green);color:var(--white);font-size:13px;font-weight:600;padding:7px 16px;border-radius:3px}
.welcome .btn{position:absolute;right:0;top:246px}
.portraits{position:absolute;left:730px;top:1190px;width:340px}
.portrait{display:flex;gap:14px;margin-top:22px}
.portrait-photo{width:78px;height:78px;flex:none;border-radius:3px}
.portrait h4{font-size:14px;color:var(--ink)}
.portrait p{font-size:12px;line-height:1.6;color:var(--muted)}

/* gallery */
.gallery{position:absolute;left:0;top:1480px;width:1200px;height:280px;background:var(--band)}
.gallery h2{text-align:center;color:var(--white);font-size:26px;font-weight:600;margin-top:22px}
.gallery-track{position:absolute;left:140px;top:80px;display:flex;gap:12px}
.gallery-item{width:174px;height:140px;border:4px solid var(--white);position:relative}
.gallery-item span{position:absolute;left:0;right:0;top:50px;text-align:center;color:var(--white);font-weight:800;font-size:13px;background:rgba(0,0,0,.35);padding:6px 0}
.g-arrow{position:absolute;top:132px;width:30px;height:30px}

/* clients */
.clients{position:absolute;left:0;top:1780px;width:1200px;height:180px}
.clients h2{display:flex;align-items:center;justify-content:center;gap:18px;font-size:26px;font-weight:600;color:var(--ink)}
.clients h2::before,.clients h2::after{content:"";width:380px;height:1px;background:#ccc}
.clients h2 b{color:var(--green);font-weight:600}
.client-row{position:absolute;left:130px;top:72px;width:940px;display:flex;justify-content:space-between;align-items:center}
.client{display:flex;align-items:center;gap:8px;font-size:14px;font-weight:700;color:var(--client)}
.client i{width:26px;height:26px;background:var(--client);display:block}
.client .badge{width:26px;height:26px;background:#e8a020;display:block}

/* footer */
.site-footer{position:absolute;left:0;top:1960px;width:1200px;height:194px;background:var(--dark);color:#ccc}
.f-col{position:absolute;top:22px}
.f-col h5{font-size:14px;color:var(--white);font-weight:600;margin-bottom:10px}
.f-col ul{list-style:none;font-size:12px;line-height:1.75}
.field{width:200px;height:22px;background:var(--white);border-radius:2px;margin-bottom:7px}
.field.area{height:44px}
.f-col .btn{padding:4px 14px;font-size:12px}
.contact-line{display:flex;align-items:flex-start;gap:10px;font-size:12px;line-height:1.5;margin-bottom:10px}
.contact-line svg{flex:none;margin-top:2px}
.copyright{position:absolute;left:0;top:2154px;width:1200px;height:30px;background:var(--darker);color:#999;font-size:11px;text-align:center;line-height:30px}
</style>
</head>
<body>

<header class="site-header">
  <div class="brand"><span class="brand-mark"></span><div class="brand-name">Verdant Field</div></div>
  <div class="social"><span></span><span></span><span></span><span></span></div>
  <nav class="main-nav">
    <a class="active">Home</a><a>About Us</a><a>Service</a><a>People</a><a>Clients</a><a>Contact</a>
  </nav>
</header>

<section class="hero" role="img" aria-label="Two consultants in blue hard hats reviewing a site">
  <div class="hero-arrow" style="left:50px"><svg width="34" height="34"><path d="M20 10l-7 7 7 7" stroke="#fff" stroke-width="3" fill="none"/></svg></div>
  <div class="hero-arrow" style="right:50px"><svg width="34" height="34"><path d="M14 10l7 7-7 7" stroke="#fff" stroke-width="3" fill="none"/></svg></div>
  <p class="hero-text">We are client focussed, offering highly experienced people providing effective and innovative environmental solutions</p>
</section>

<section class="services" role="img" aria-label="Green field under a dark blue sky">
  <article class="card" style="left:130px">
    <h3>Project Management</h3>
    <div class="card-photo" role="img" aria-label="Meeting around a table" style="background:linear-gradient(#c9c2b4,#8e8677)"></div>
    <ul><li>Risk advice</li><li>Scope of services and costing</li><li>Technical specifications</li><li>Tendering support</li></ul>
  </article>
  <article class="card" style="left:370px">
    <h3>Contaminated Land</h3>
    <div class="card-photo" role="img" aria-label="Worker sampling soil on site" style="background:linear-gradient(#9cc1d6,#b87a3c)"></div>
    <ul><li>Stage one preliminary assessment</li><li>Stage two detailed assessment</li><li>Site remediation plans</li><li>Validation reporting</li></ul>
  </article>
  <article class="card" style="left:610px">
    <h3>Hazardous Materials &amp; Occupational Hygiene</h3>
    <div class="card-photo" role="img" aria-label="Worker in protective suit" style="background:linear-gradient(#e8e4a0,#c9b63a)"></div>
    <ul><li>Hazardous materials surveys</li><li>Asbestos management plans</li><li>Indoor air quality review</li></ul>
  </article>
  <article class="card" style="left:850px">
    <h3>Environmental Assessment and Management</h3>
    <div class="card-photo" role="img" aria-label="Field officer in high visibility vest" style="background:linear-gradient(#d6d98a,#6a8a3a)"></div>
    <ul><li>Waste management</li><li>Landfill monitoring</li><li>Ecological assessment</li><li>Erosion and sediment control</li></ul>
  </article>
</section>

<section class="welcome">
  <h2 class="section-head">Welcome To <b>Verdant Field</b></h2>
  <p>We are a small Australian consultancy helping clients understand and manage their environmental obligations. Our team brings many years of field and office experience across government, mining, construction and property sectors. We listen closely, plan carefully and deliver clear, practical advice that keeps projects moving while protecting land, water and people. From early site checks to long term monitoring, we tailor each service to the scale of the job, keep costs transparent and stay in touch at every stage so that our clients always know where their project stands and what comes next.</p>
  <span class="btn">Read More &rsaquo;</span>
</section>

<section class="portraits">
  <h2 class="section-head">Pen <b>Portrait</b></h2>
  <div class="portrait">
    <div class="portrait-photo" role="img" aria-label="Portrait of Marcus Hale" style="background:linear-gradient(#bda58c,#6b5644)"></div>
    <div><h4>Marcus Hale</h4><p>Principal consultant with twenty years in contaminated land and site remediation across Australia.</p></div>
  </div>
  <div class="portrait">
    <div class="portrait-photo" role="img" aria-label="Portrait of Owen Pryor" style="background:linear-gradient(#c4b29e,#5e5a55)"></div>
    <div><h4>Owen Pryor</h4><p>Senior occupational hygienist leading hazardous materials surveys and air quality programs.</p></div>
  </div>
</section>

<section class="gallery">
  <h2>Projects Gallery</h2>
  <svg class="g-arrow" style="left:92px" viewBox="0 0 30 30"><path d="M19 6l-9 9 9 9" stroke="#fff" stroke-width="3" fill="none"/></svg>
  <div class="gallery-track">
    <div class="gallery-item" role="img" aria-label="Team meeting" style="background:linear-gradient(#dfe6ea,#8fa3b0)"></div>
    <div class="gallery-item" role="img" aria-label="Site inspection" style="background:linear-gradient(#9fc1d8,#6c8f5a)"></div>
    <div class="gallery-item" role="img" aria-label="Contaminated land works" style="background:linear-gradient(#8aa4b8,#5d6e3e)"><span>CONTAMINATED LAND</span></div>
    <div class="gallery-item" role="img" aria-label="Sunlit landscape" style="background:linear-gradient(#3a6fb0,#e0a040)"></div>
    <div class="gallery-item" role="img" aria-label="Canola field" style="background:linear-gradient(#8fb6e0,#e6d22a)"></div>
  </div>
  <svg class="g-arrow" style="left:1078px" viewBox="0 0 30 30"><path d="M11 6l9 9-9 9" stroke="#fff" stroke-width="3" fill="none"/></svg>
</section>

<section class="clients">
  <h2>Our <b>Clients</b></h2>
  <div class="client-row">
    <div class="client"><i></i>Bluecrest</div>
    <div class="client"><i></i>Ridgeline Resources</div>
    <div class="client"><i style="border-radius:50%"></i>Coralpoint</div>
    <div class="client"><i></i>Kestrel Energy</div>
    <div class="client">Northgate Build</div>
    <div class="client"><span class="badge"></span></div>
  </div>
</section>

<footer class="site-footer">
  <div class="f-col" style="left:130px">
    <h5>Quick Links</h5>
    <ul><li>Home</li><li>About Us</li><li>Services</li><li>People</li><li>Clients</li><li>Contact Us</li></ul>
  </div>
  <div class="f-col" style="left:320px">
    <h5>Quick Inquiry</h5>
    <div class="field"></div><div class="field"></div><div class="field area"></div>
    <span class="btn">SUBMIT</span>
  </div>
  <div class="f-col" style="left:600px">
    <h5>Contact Details</h5>
    <div class="contact-line"><svg width="14" height="16" viewBox="0 0 14 16"><path d="M7 0a6 6 0 0 1 6 6c0 4-6 10-6 10S1 10 1 6a6 6 0 0 1 6-6z" fill="#8dc63f"/></svg><span>Verdant Field<br>Suite 4, 12 Harbour Lane<br>Brisbane QLD 4000</span></div>
    <div class="contact-line"><svg width="14" height="14" viewBox="0 0 14 14"><path d="M3 1l3 3-2 2c1 2 2 3 4 4l2-2 3 3-2 2C6 13 1 8 1 3z" fill="#8dc63f"/></svg><span>555-0142-318</span></div>
    <div class="contact-line"><svg width="14" height="14" viewBox="0 0 14 14"><path d="M3 1l3 3-2 2c1 2 2 3 4 4l2-2 3 3-2 2C6 13 1 8 1 3z" fill="#8dc63f"/></svg><span>555-0142-319</span></div>
    <div class="contact-line"><svg width="14" height="12" viewBox="0 0 14 12"><rect x="0.5" y="0.5" width="13" height="11" fill="none" stroke="#8dc63f"/><path d="M1 1l6 5 6-5" stroke="#8dc63f" fill="none"/></svg><span>hello@verdantfield.example</span></div>
  </div>
</footer>
<div class="copyright">Copyright 2014 Verdant Field. All Rights Reserved.</div>

</body>
</html>
```